Business card and Logo design Round 2

Hello Everyone,

We would like to get a redesign of our LOGO and Business card. Required for this project.

New Logo design, Several options of business card and at least 3 to 4 banner designs.

I am attaching our current Logo and business card for your reference and Information only.

We required png, pdf, jpg and Adobe formats.

```html
<!DOCTYPE html>
<html lang="en">
<head>
<meta charset="utf-8">
<title>Velmor Development — Business Card</title>
<link rel="stylesheet" href="https://fonts.googleapis.com/css2?family=Noto+Serif:wght@400;700&family=Open+Sans:wght@400;600;700&display=swap">
<style>
  :root {
    --backdrop: #2c3442;
    --card: #f7f7f5;
    --ink: #111111;
    --band: #0d0d0d;
    --band-text: #e9e9e9;
    --muted: #333333;
  }
  * { box-sizing: border-box; margin: 0; padding: 0; }
  html, body { width: 1200px; height: 849px; overflow: hidden; }
  body {
    background: var(--backdrop);
    position: relative;
    font-family: "Open Sans", sans-serif;
  }
  .card {
    position: absolute;
    background: var(--card);
    overflow: hidden;
    box-shadow: 0 18px 40px rgba(0,0,0,0.35);
  }

  /* Back: name and contacts, portrait */
  .card-back {
    left: 150px; top: 150px;
    width: 310px; height: 540px;
  }
  .person {
    position: absolute;
    top: 130px; left: 0; right: 0;
    text-align: center;
  }
  .person-name {
    font-family: "Noto Serif", serif;
    font-weight: 700;
    font-size: 24px;
    color: var(--ink);
    letter-spacing: 0.3px;
  }
  .person-role {
    font-family: "Noto Serif", serif;
    font-size: 12px;
    color: var(--muted);
    margin-top: 4px;
  }
  .contact-band {
    position: absolute;
    left: 0; right: 0; bottom: 0;
    height: 170px;
    background: var(--band);
    padding: 30px 0 0 48px;
  }
  .contact-list { list-style: none; }
  .contact-item {
    display: flex;
    align-items: center;
    gap: 16px;
    color: var(--band-text);
    font-size: 14px;
    height: 28px;
  }
  .contact-icon { width: 16px; height: 16px; flex: none; }

  /* Front: logo and address, landscape */
  .card-front {
    left: 560px; top: 230px;
    width: 520px; height: 300px;
  }
  .front-band {
    position: absolute;
    left: 0; right: 0; top: 0;
    height: 46px;
    background: var(--band);
  }
  .brand {
    position: absolute;
    left: 0; right: 0; top: 92px;
    display: flex;
    justify-content: center;
    align-items: center;
    gap: 14px;
  }
  .brand-square {
    width: 34px; height: 34px;
    background: var(--ink);
  }
  .brand-name {
    font-family: "Open Sans", sans-serif;
    font-weight: 700;
    font-size: 40px;
    color: var(--ink);
    letter-spacing: 2px;
  }
  .company-details {
    position: absolute;
    left: 0; right: 0; top: 176px;
    text-align: center;
    font-size: 13px;
    color: var(--muted);
    line-height: 1.55;
  }
</style>
</head>
<body>

  <section class="card card-back">
    <div class="person">
      <p class="person-name">Daniel Roarke</p>
      <p class="person-role">CEO</p>
    </div>
    <div class="contact-band">
      <ul class="contact-list">
        <li class="contact-item">
          <svg class="contact-icon" viewBox="0 0 24 24" fill="currentColor"><path d="M6.6 10.8a15.1 15.1 0 0 0 6.6 6.6l2.2-2.2c.3-.3.7-.4 1-.2 1.1.4 2.3.6 3.6.6.6 0 1 .4 1 1V20c0 .6-.4 1-1 1A17 17 0 0 1 3 4c0-.6.4-1 1-1h3.5c.6 0 1 .4 1 1 0 1.3.2 2.5.6 3.6.1.3 0 .7-.2 1z"/></svg>
          <span>555-214-0387</span>
        </li>
        <li class="contact-item">
          <svg class="contact-icon" viewBox="0 0 24 24" fill="currentColor"><path d="M3 8c0-2 4-4 9-4s9 2 9 4v2h-5V8.5c-1-.5-2.5-.7-4-.7s-3 .2-4 .7V10H3z"/><rect x="5" y="12" width="14" height="8" rx="1"/></svg>
          <span>555-260-4411</span>
        </li>
        <li class="contact-item">
          <svg class="contact-icon" viewBox="0 0 24 24" fill="none" stroke="currentColor" stroke-width="2"><rect x="3" y="5" width="18" height="14"/><path d="M3 5l9 8 9-8M3 19l7-7M21 19l-7-7"/></svg>
          <span>droarke@velmorbuild.com</span>
        </li>
        <li class="contact-item">
          <svg class="contact-icon" viewBox="0 0 24 24" fill="none" stroke="currentColor" stroke-width="1.8"><circle cx="12" cy="12" r="9"/><ellipse cx="12" cy="12" rx="4" ry="9"/><path d="M3 12h18"/></svg>
          <span>www.velmorbuild.com</span>
        </li>
      </ul>
    </div>
  </section>

  <section class="card card-front">
    <div class="front-band"></div>
    <div class="brand">
      <span class="brand-square"></span>
      <span class="brand-name">VELMOR</span>
    </div>
    <div class="company-details">
      <p>Velmor Development Inc.</p>
      <p>42 Harlow Street, Fairview, BC</p>
    </div>
  </section>

</body>
</html>
```